Landscape Supplier and Excavation company needing a website revamp.

We need a web design for our company based out of northern Virginia. We make and deliver topsoil, mulch, and compost. We are also an excavation company. We provide a wide variety of excavation services, from residential to large commercial projects. We specialize in land clearing and building site preparation. We would like a site that looks very professional and makes us look like a large company. We've been in business since 1994 and have never had a really nice website. Our current website it www.harrowfieldloam.com and www.pvrqx.com for references. I like the information on the pages but would like something more professional looking. Doesn't HAVE to be 4 different pages, but I would like a contact form, our services, and our products/ pricing listed. We are properly licensed and insured and would like this included somewhere on the site.

Target Market(s)

Landscapers, Home Owners, Commercial

Industry/Entity Type

Excavation and Landscape Products Supplier

Number of Pages Required

4 page

Colors

Designer to choose colors to be used in the design.

Requirements
Must have
• Professional Look and Feel

```html
<!DOCTYPE html>
<html lang="en">
<head>
<meta charset="utf-8">
<title>Harrowfield Loam and Excavation</title>
<link rel="stylesheet" href="https://fonts.googleapis.com/css2?family=Barlow+Semi+Condensed:wght@600;700&family=Open+Sans:wght@400;600&family=Poppins:wght@400;500;600&display=swap">
<style>
:root{
  --red:#bb1e27;
  --red-deep:#a51820;
  --dark:#25252b;
  --dark-card:#2d2d33;
  --light:#f0f0f0;
  --white:#ffffff;
  --ink:#333338;
  --muted:#9a9aa0;
  --field:#f4f4f4;
  --navy:#1d1e3a;
}
*{box-sizing:border-box;margin:0;padding:0}
html,body{width:1200px;height:2805px;overflow:hidden}
body{position:relative;background:var(--white);font-family:"Open Sans",sans-serif;color:var(--ink)}
.abs{position:absolute}

/* header */
.site-header{position:absolute;left:0;top:0;width:1200px;height:74px;background:var(--white)}
.brand{position:absolute;left:210px;top:16px;width:179px;height:38px;display:flex;align-items:center;gap:8px}
.brand-mark{width:12px;height:12px;background:var(--red)}
.brand-name{font-family:"Poppins",sans-serif;font-weight:600;font-size:13px;color:var(--red);line-height:1.1}
.main-nav{position:absolute;top:28px;left:513px;display:flex;gap:29px;font-family:"Poppins",sans-serif;font-weight:500;font-size:13px;color:#222}
.main-nav .active{color:var(--red)}

/* hero */
.hero{position:absolute;left:0;top:74px;width:1200px;height:484px;background:var(--white)}
.hero-photo{position:absolute;inset:0;clip-path:polygon(0 0,570px 0,732px 238px,566px 484px,0 484px);
  background:linear-gradient(160deg,#4d6782 0%,#c98b45 38%,#f2c36e 52%,#a86a33 72%,#6b4526 100%)}
.hero-work{position:absolute;inset:0;background:var(--dark);clip-path:polygon(600px 0,1200px 0,1200px 226px,754px 226px)}
.hero-call{position:absolute;inset:0;clip-path:polygon(754px 251px,1200px 251px,1200px 484px,598px 484px);
  background:linear-gradient(110deg,#9e1b24 0%,#c42a33 55%,#a71d25 100%)}
.work-title{left:763px;top:54px;font-family:"Barlow Semi Condensed",sans-serif;font-weight:700;font-size:30px;letter-spacing:2px;color:var(--red)}
.work-bar{left:764px;top:96px;width:24px;height:3px;background:var(--red)}
.work-text{left:764px;top:124px;width:400px;font-size:12.5px;line-height:20px;color:var(--muted)}
.call-text{left:769px;top:320px;font-family:"Barlow Semi Condensed",sans-serif;font-weight:700;font-size:44px;letter-spacing:3px;line-height:54px;color:var(--white)}

/* services */
.services{position:absolute;left:0;top:558px;width:1200px;height:366px;background:var(--dark)}
.section-title{font-family:"Barlow Semi Condensed",sans-serif;font-weight:700;font-size:31px;text-align:center}
.services .section-title{position:absolute;top:38px;width:100%;color:var(--white)}
.svc-card{position:absolute;top:114px;width:247px;height:162px;background:var(--dark-card);text-align:center;padding:32px 26px 0}
.svc-card h3{font-weight:600;font-size:12.5px;color:var(--white);margin-bottom:8px}
.svc-card p{font-size:9.5px;line-height:16px;color:var(--muted)}
.svc-card a{display:block;margin-top:10px;font-size:9.5px;color:var(--red);text-decoration:none}
.svc-card.featured{background:var(--red)}
.svc-card.featured p,.svc-card.featured a{color:var(--white)}
.svc-nav{position:absolute;top:297px;width:37px;height:36px;border:1px solid #55555b;display:flex;align-items:center;justify-content:center}
.btn-solid{position:absolute;background:var(--red);color:var(--white);font-family:"Poppins",sans-serif;font-size:9.5px;letter-spacing:2px;font-weight:500;display:flex;align-items:center;justify-content:center}

/* about */
.about{position:absolute;left:0;top:924px;width:1200px;height:567px;background:var(--light)}
.about-photo{position:absolute;left:210px;top:131px;width:310px;height:302px;border:3px solid #6e6e70;
  background:linear-gradient(180deg,#a9c3de 0%,#cfdbe6 26%,#7b7a55 34%,#a68c66 55%,#8a6e4d 100%);
  box-shadow:18px 20px 40px rgba(0,0,0,.18)}
.about-title{left:611px;top:136px;font-family:"Barlow Semi Condensed",sans-serif;font-weight:700;font-size:35px;color:var(--ink)}
.about-sub{left:611px;top:176px;font-family:"Barlow Semi Condensed",sans-serif;font-weight:600;font-size:20px;color:var(--ink)}
.about-bar{left:611px;top:210px;width:23px;height:3px;background:var(--red)}
.about-text{left:611px;top:226px;width:385px;font-size:9.6px;line-height:20px;color:#3a3a3e}
.about-text p+p{margin-top:7px}
.btn-outline{position:absolute;border:1.5px solid var(--red);color:var(--red);font-family:"Poppins",sans-serif;font-size:9.5px;letter-spacing:2px;display:flex;align-items:center;justify-content:center}

/* contact */
.contact{position:absolute;left:0;top:1491px;width:1200px;height:830px;
  background:radial-gradient(ellipse at 70% 20%,#c8313a 0%,rgba(200,49,58,0) 45%),radial-gradient(ellipse at 20% 70%,#c42b34 0%,rgba(196,43,52,0) 45%),var(--red-deep)}
.contact-title{position:absolute;top:93px;width:100%;text-align:center;font-family:"Poppins",sans-serif;font-weight:600;font-size:25px;line-height:32px;color:var(--white)}
.form-card{position:absolute;left:247px;top:1727px;width:706px;height:743px;background:var(--white)}
.form-card h2{position:absolute;top:74px;width:100%;text-align:center;font-family:"Poppins",sans-serif;font-weight:500;font-size:27px;color:var(--navy)}
.form-intro{position:absolute;top:128px;width:100%;text-align:center;font-family:"Poppins",sans-serif;font-size:10px;line-height:14px;color:#66666c}
.field{position:absolute;left:80px;width:546px;height:55px;background:var(--field);border:1px solid #d9d9d9;
  font-family:"Poppins",sans-serif;font-size:12.5px;color:#77777c;padding:18px 20px}
.submit{position:absolute;left:80px;top:594px;width:546px;height:70px;background:var(--red);color:var(--white);
  font-family:"Poppins",sans-serif;font-weight:500;font-size:16px;display:flex;align-items:center;justify-content:center}

/* footer */
.site-footer{position:absolute;left:0;top:2321px;width:1200px;height:484px;background:var(--dark)}
.form-wrap-over{}
.foot-head{position:absolute;top:222px;font-family:"Poppins",sans-serif;font-size:15px;color:var(--red)}
.foot-text{position:absolute;font-family:"Poppins",sans-serif;font-size:9.5px;line-height:14px;color:#a7a7ad}
.foot-list{position:absolute;top:269px;list-style:none;font-family:"Poppins",sans-serif;font-size:10px;line-height:25px;color:#a7a7ad}
.newsletter-input{position:absolute;left:845px;top:291px;width:215px;height:39px;background:#2d2d33;font-family:"Poppins",sans-serif;font-size:8.5px;color:#a7a7ad;padding:14px 17px}
.newsletter-btn{position:absolute;left:845px;top:2672px}
.foot-rule{position:absolute;left:146px;top:428px;width:914px;height:1px;background:#4a4a50}
.foot-bottom{position:absolute;top:449px;font-family:"Poppins",sans-serif;font-size:9.5px;color:#a7a7ad}
</style>
</head>
<body>

<header class="site-header">
  <div class="brand"><span class="brand-mark"></span><span class="brand-name">Harrowfield Loam<br>and Excavation</span></div>
  <nav class="main-nav">
    <span class="active">HOME</span><span>ABOUT US</span><span>SERVICES</span><span>PRODUCTS/PRICING</span><span>CONTACT US</span>
  </nav>
</header>

<section class="hero">
  <div class="hero-photo" role="img" aria-label="Excavator digging earth at sunset"></div>
  <div class="hero-work"></div>
  <div class="hero-call" role="img" aria-label="Red-toned photo of a hand holding a phone handset"></div>
  <h2 class="abs work-title">RECENT WORK</h2>
  <div class="abs work-bar"></div>
  <p class="abs work-text">We provide a wide variety of excavation services, from residential to large commercial projects. We specialize in land clearing and building site preparation.</p>
  <p class="abs call-text">CALL US<br>703-555-0187</p>
</section>

<section class="services">
  <h2 class="section-title">OUR SERVICES</h2>
  <article class="svc-card" style="left:210px">
    <h3>EXCAVATION</h3>
    <p>services, from residential to large commercial projects. We specialize in land clearing and building site preparation.</p>
    <a>View details</a>
  </article>
  <article class="svc-card" style="left:477px">
    <h3>DEMOLITION</h3>
    <p>We specialize in demolition projects. From tearing down and removing an old home to clearing the site.</p>
    <a>View details</a>
  </article>
  <article class="svc-card featured" style="left:744px">
    <h3>TOPSOIL</h3>
    <p>Our emphasis is to produce the very best quality topsoil for the best results! Our topsoil and organics make quality</p>
    <a>View details</a>
  </article>
  <div class="svc-nav" style="left:506px"><svg width="10" height="14" viewBox="0 0 10 14"><path d="M8 1 2 7l6 6" fill="none" stroke="#bb1e27" stroke-width="2"/></svg></div>
  <div class="btn-solid" style="left:556px;top:297px;width:88px;height:36px">SHOW ALL</div>
  <div class="svc-nav" style="left:657px"><svg width="10" height="14" viewBox="0 0 10 14"><path d="M2 1l6 6-6 6" fill="none" stroke="#bb1e27" stroke-width="2"/></svg></div>
</section>

<section class="about">
  <div class="about-photo" role="img" aria-label="Loader feeding a soil screening machine at a work site"></div>
  <h2 class="abs about-title">ABOUT US</h2>
  <h3 class="abs about-sub">MARKETING GUIDE</h3>
  <div class="abs about-bar"></div>
  <div class="abs about-text">
    <p>A leading Excavating Contractor in the NOVA area. I provide my clients with a comprehensive approach to contracting and specialize in a wide range of services. Ever since starting out as a professional Excavating Contractor, I've prioritized serving my clients' needs and satisfaction above everything else.I take care of all the small details so you don't have to. Get in touch to bring your vision to life today!</p>
    <p>Our emphasis is to produce the very best quality topsoil for the best results! Our topsoil and organics make quality ready-made soils and lawn amendments.</p>
  </div>
  <div class="btn-solid" style="left:611px;top:386px;width:94px;height:36px">SEE MORE</div>
  <div class="btn-outline" style="left:724px;top:386px;width:103px;height:36px">DOWNLOAD</div>
</section>

<section class="contact">
  <h2 class="contact-title">CONTACT US TODAY FOR ALL OF YOUR<br>TOPSOIL AND EXCAVATION NEEDS</h2>
</section>

<footer class="site-footer">
  <h4 class="foot-head" style="left:146px">About Us</h4>
  <p class="foot-text" style="left:146px;top:272px;width:260px">A leading Excavating Contractor in the NOVA area. I provide my clients with a comprehensive approach to contracting and specialize in a wide range of services.</p>
  <p class="foot-text" style="left:146px;top:340px">1420 Birch Hollow Rd, Marshall, VA 20115.</p>
  <p class="foot-text" style="left:146px;top:365px">540-555-0142</p>
  <p class="foot-text" style="left:146px;top:390px">example@pvrqx.com</p>

  <h4 class="foot-head" style="left:465px">Quicklinks</h4>
  <ul class="foot-list" style="left:465px"><li>› Blog</li><li>› Help Center</li><li>› Community</li><li>› Career</li><li>› About Us</li></ul>

  <h4 class="foot-head" style="left:656px">Our Company</h4>
  <ul class="foot-list" style="left:656px"><li>› Our Company</li><li>› Portfolio</li><li>› Praivacy Policy</li><li>› Latest Blog</li><li>› Carrer</li></ul>

  <h4 class="foot-head" style="left:845px">Newsletter</h4>
  <p class="foot-text" style="left:843px;top:272px">Subscribe our Newsletter for any updates</p>
  <div class="newsletter-input">Enter Your Email</div>
  <div class="btn-solid" style="left:844px;top:351px;width:86px;height:31px;font-size:11.5px;letter-spacing:0;font-weight:600">Submit</div>

  <div class="foot-rule"></div>
  <p class="foot-bottom" style="left:146px">©2021 pvrqx. All rights reserved</p>
  <p class="foot-bottom" style="left:804px">Terms &amp; Condition &nbsp;&nbsp;|&nbsp;&nbsp; Privacy Policy &nbsp;&nbsp;|&nbsp;&nbsp; Contact Us</p>
</footer>

<div class="form-card">
  <h2>Send A message</h2>
  <p class="form-intro">Lorem Ipsum is simply dummy text of the printing and typesetting industry. Lorem Ipsum<br>has been the industry's standard dummy text ever since the 1500s,</p>
  <div class="field" style="top:197px">First Name:</div>
  <div class="field" style="top:265px">Last Name:</div>
  <div class="field" style="top:332px">Email:</div>
  <div class="field" style="top:400px;height:166px">Message:</div>
  <div class="submit">Submit Message</div>
</div>

</body>
</html>
```